Introduction of new dentist and new treatments

We want inform our Patients of our new dentist and new treatment methods. It is dealing about biologic dentistry and holistic dentistry. we are in switzerland and speak german

Font styles to use
Sans Serif

Colors
00a990
33b8a4
9bcb3c
acd036
cadf82
0292cd
3176b5
e34297
e667a6

Requirements
Must have
• Text, which can be edited. It will be in german
• Name of the dental clinic is
• "Brivana - Ihr Zahnarzt in Zug"
Nice to have
• A4 Layout

```html
<!DOCTYPE html>
<html lang="de">
<head>
<meta charset="utf-8">
<title>Brivana – Ihr Zahnarzt in Zug</title>
<link rel="stylesheet" href="https://fonts.googleapis.com/css2?family=PT+Sans:wght@400;700&family=Tinos&display=swap">
<style>
  :root {
    --navy: #1c3566;
    --navy-dark: #183462;
    --blue: #1f73c0;
    --wave-blue: #3a87c8;
    --wave-light: #a9dbe6;
    --pink: #e667a6;
    --paper: #eef6f8;
    --text: #555a60;
    --ring: #4a5a8a;
  }
  * { margin: 0; padding: 0; box-sizing: border-box; }
  html, body { width: 962px; height: 1200px; overflow: hidden; background: #ffffff; }
  .flyer {
    position: relative; width: 962px; height: 1200px;
    background: var(--paper); font-family: "PT Sans", sans-serif; color: var(--text);
  }
  .hero { position: absolute; left: 0; top: 0; width: 962px; height: 540px; }
  .brand {
    position: absolute; left: 0; width: 370px; top: 382px; text-align: center;
  }
  .brand-name {
    font-family: "PT Sans", sans-serif; font-size: 44px; letter-spacing: 8px;
    color: var(--navy); font-weight: 400; display: inline-flex; align-items: center; gap: 14px;
  }
  .brand-dot { width: 16px; height: 16px; border-radius: 50%; background: var(--navy); display: inline-block; }
  .brand-tagline {
    font-size: 20px; font-weight: 700; color: var(--navy); margin-top: 6px; padding-left: 90px; text-align: left;
  }
  .intro-title {
    position: absolute; left: 30px; right: 30px; top: 540px; text-align: center;
    font-family: "Tinos", serif; font-size: 26px; line-height: 31px; color: var(--blue);
  }
  .intro-text {
    position: absolute; left: 48px; right: 40px; top: 610px;
    font-size: 16.5px; line-height: 21px; color: var(--navy-dark);
  }
  .topic { position: absolute; width: 446px; }
  .topic-head { display: flex; align-items: center; gap: 10px; margin-bottom: 6px; min-height: 40px; }
  .topic-icon { width: 34px; height: 34px; flex: none; }
  .topic-title { font-size: 17px; line-height: 18px; color: var(--navy); }
  .topic-text { font-size: 13.4px; line-height: 15.6px; text-align: justify; hyphens: auto; }
  .topic-kauorgan { left: 26px; top: 688px; }
  .topic-parodontitis { left: 490px; top: 688px; }
  .topic-zahnverlust { left: 24px; top: 922px; }
  .topic-ganzheitlich { left: 490px; top: 922px; }
  .footer {
    position: absolute; left: 0; bottom: 0; width: 962px; height: 80px;
    background: var(--navy-dark); color: #ffffff; font-size: 15.5px;
    display: flex; align-items: center; justify-content: space-between; padding: 0 32px 0 26px;
  }
  .footer-item { display: flex; align-items: center; gap: 9px; }
  .footer-item svg { width: 16px; height: 16px; }
  .footer-rule { position: absolute; left: 0; bottom: 80px; width: 962px; height: 3px; background: var(--wave-light); }
</style>
</head>
<body>
<main class="flyer">
  <svg class="hero" viewBox="0 0 962 540" xmlns="http://www.w3.org/2000/svg">
    <defs>
      <linearGradient id="photoTone" x1="0" y1="0" x2="1" y2="1">
        <stop offset="0" stop-color="#c9c39a"/>
        <stop offset="0.45" stop-color="#e3c7b4"/>
        <stop offset="1" stop-color="#d8c25a"/>
      </linearGradient>
      <linearGradient id="portraitTone" x1="0" y1="0" x2="0" y2="1">
        <stop offset="0" stop-color="#f2f2f2"/>
        <stop offset="0.6" stop-color="#d9b8a0"/>
        <stop offset="1" stop-color="#2c6fc0"/>
      </linearGradient>
    </defs>
    <rect role="img" aria-label="Foto einer lächelnden Familie über drei Generationen im Freien" x="0" y="0" width="962" height="520" fill="url(#photoTone)"/>
    <path d="M0,252 C110,210 290,205 410,290 C510,360 560,450 660,492 L0,520 Z" fill="#ffffff"/>
    <path d="M0,470 C200,500 420,470 620,430 C760,405 880,400 962,410 L962,450 C860,445 760,460 620,480 C420,510 200,520 0,500 Z" fill="var(--wave-blue)"/>
    <path d="M0,485 C200,515 430,490 640,460 C780,442 880,440 962,448 L962,540 L0,540 Z" fill="var(--wave-light)"/>
    <path d="M0,500 C200,525 440,505 650,478 C790,462 890,460 962,466 L962,540 L0,540 Z" fill="var(--paper)"/>
    <circle cx="824" cy="408" r="118" fill="var(--ring)"/>
    <circle role="img" aria-label="Porträtfoto des neuen Zahnarztes" cx="824" cy="408" r="104" fill="url(#portraitTone)"/>
  </svg>

  <header class="brand">
    <div class="brand-name"><span class="brand-dot"></span>BRIVANA</div>
    <div class="brand-tagline">Ihr Zahnarzt in Zug</div>
  </header>

  <h1 class="intro-title">Interdisziplinäre Zahnmedizin - Zusammenhang zwischen Zahnproblemen<br>und der Gesundheit von Körper und Geist</h1>
  <p class="intro-text">Zahn und Gesundheit haben eins gemeinsam – Man vermisst sie, wenn sie fehlt. Zähne haben einen engen Zusammenhang zur Gesundheit und können diese beeinflussen. Sowohl negativ als auch positiv.</p>

  <section class="topic topic-kauorgan">
    <div class="topic-head">
      <svg class="topic-icon" role="img" aria-label="Symbol Lupe und Zahn" viewBox="0 0 34 34"><circle cx="14" cy="14" r="9" fill="none" stroke="var(--pink)" stroke-width="3"/><line x1="8" y1="22" x2="2" y2="30" stroke="var(--pink)" stroke-width="4"/><rect x="22" y="8" width="10" height="20" rx="4" fill="var(--wave-light)"/></svg>
      <h2 class="topic-title">Funktion des Kauorgans<br>und interdisziplinäre Zahnmedizin</h2>
    </div>
    <p class="topic-text">„Funktion ist nicht alles. Aber ohne Funktion ist alles nichts!“ Sagte einst Prof.A.Hallberg(Zahnarzt, Gnathologie) und betonte die Bedeutung der Funktion des Kausystems. Sprechen, Kauen aber auch Körperhaltung und Stressmanagement gehören zu den Funktionen der Zähne. Ein gut funktionierendes Kauorgan (nach Prof.R. Vandrik, interdisziplinäre Zahnmedizin) kann Stress bewältigen und mehr Leistung und Wohlbefinden bringen. Sehr oft erkennt man Funktionsstörungen daran, dass die Zähne nicht richtig zueinander passen oder Muskelverspannungen und Schmerzen im Kiefergelenk auftreten.</p>
  </section>

  <section class="topic topic-parodontitis">
    <div class="topic-head">
      <svg class="topic-icon" role="img" aria-label="Symbol Zahn mit Zahnfleisch" viewBox="0 0 34 34"><rect x="10" y="2" width="14" height="18" rx="5" fill="var(--wave-light)"/><rect x="4" y="18" width="26" height="12" rx="4" fill="var(--pink)"/></svg>
      <h2 class="topic-title">Parodontitis und<br>systemische Erkrankungen</h2>
    </div>
    <p class="topic-text">Parodontitis (Entzündung des Zahnhalteapparats) ist eine der häufigsten chronischen Krankheiten weltweit und daher gut erforscht. Herzkrankheiten, Diabetes und Frühgeburtlichkeit sind einige der systemischen Krankheiten mit der Parodontitis in Zusammenhang steht.Zahnfleischbluten, Zahnlockerung, Zahnfleischschwund und Zahnverlust sind typische Begleiterscheinungen von Parodontitis. Eine systematische Parodontitis-Behandlung kann auchpositive Auswirkungen auf die gesamte Gesundheit haben.</p>
  </section>

  <section class="topic topic-zahnverlust">
    <div class="topic-head">
      <svg class="topic-icon" role="img" aria-label="Symbol Zahn" viewBox="0 0 34 34"><rect x="8" y="3" width="18" height="28" rx="7" fill="var(--wave-light)"/><circle cx="20" cy="11" r="3" fill="var(--pink)"/></svg>
      <h2 class="topic-title">Zahnverlust und<br>neurologische Auswirkung</h2>
    </div>
    <p class="topic-text">Ein physiologisches Kausystem hat sehr feine Steuerungs- und Wahrnehmungsmöglichkeiten. Bei Zahnverlust werden diese Fähigkeiten weniger benötigt. Weniger gebrauchte Ressourcen werden von der Natur dementsprechend abgebaut. Studien zeigen, dass Menschen mit weniger Zähnen mehr Risiko zur Bildung von Demenz bergen.</p>
  </section>

  <section class="topic topic-ganzheitlich">
    <div class="topic-head">
      <svg class="topic-icon" role="img" aria-label="Symbol Zahn mit Apfel" viewBox="0 0 34 34"><rect x="4" y="8" width="24" height="22" rx="9" fill="var(--wave-light)"/><circle cx="26" cy="6" r="4" fill="var(--pink)"/></svg>
      <h2 class="topic-title">Ganzheitliche Erklärungen</h2>
    </div>
    <p class="topic-text">Die komplementäre Zahnheilkunde, sehr oft auch als ganzheitliche oder biologische Zahnheilkunde bezeichnet, versucht mit Hilfe von Meridianen(Traditionelle Chinesische Medizin), den Zusammenhang zwischen Zähnen und anderen Organen und Körperteilen zu erklären. Es gibt immer mehr Patienten und Zahnärzte die von dieser Theorie und deren Ergebnissen überzeugt sind. Aufgrund der wissenschaftlichen Lage ist eine ausführliche Aufklärung vor der Behandlung sehr ratsam.</p>
  </section>

  <div class="footer-rule"></div>
  <footer class="footer">
    <div class="footer-item">
      <svg viewBox="0 0 16 16"><path d="M8 1a5 5 0 0 0-5 5c0 4 5 9 5 9s5-5 5-9a5 5 0 0 0-5-5z" fill="#fff"/><circle cx="8" cy="6" r="2" fill="var(--navy-dark)"/></svg>
      <span>Zahnarztpraxis Seestrasse 14, 6300 Zug</span>
    </div>
    <div class="footer-item">
      <svg viewBox="0 0 16 16"><circle cx="8" cy="8" r="7" fill="none" stroke="#fff" stroke-width="1.4"/><path d="M5.5 4.5l1.5 0.2 0.6 1.8-1 0.8c0.6 1.2 1.4 2 2.6 2.6l0.8-1 1.8 0.6 0.2 1.5c-3.5 0.8-7.3-3-6.5-6.5z" fill="#fff"/></svg>
      <span>+41 41 555 01 23</span>
    </div>
    <div class="footer-item">
      <svg viewBox="0 0 16 16" fill="none" stroke="#fff" stroke-width="1.2"><circle cx="8" cy="8" r="7"/><ellipse cx="8" cy="8" rx="3" ry="7"/><line x1="1" y1="8" x2="15" y2="8"/><line x1="2" y1="4.5" x2="14" y2="4.5"/><line x1="2" y1="11.5" x2="14" y2="11.5"/></svg>
      <span>www.brivana-zug.ch</span>
    </div>
  </footer>
</main>
</body>
</html>
```